Dovra's Spice Blend Dry Roasted and Freshly Ground Spices to create the Authentic and Aromatic Maur

I need a packaging design for a new company based in Kent called Dovra's Spice Blend. the size of the packaging will be for a 250gm bag.

I would like bright colours so that it can stand out from out the other products on a super market shelf

The packaging must have the list of ingredients on the back;

I.e. Ingredients;
Cumin
Coriander
Dried Red Chili
Cinnamon
Cloves
Cardamon
Black Peppercorn
Rice

Reason: Not enough designed to choose from. Dovra's Spice Blend, Dry Roasted and Freshly Ground Spices to create the Authentic and Aromatic flavour Please also add Turmeric to the ingredient list Thank you MarlaOunsworth

```html
<!DOCTYPE html>
<html lang="en">
<head>
<meta charset="utf-8">
<title>Dovra's Spice Blend – Packaging</title>
<link rel="stylesheet" href="https://fonts.googleapis.com/css2?family=Londrina+Solid:wght@900&family=Short+Stack&display=swap">
<style>
  :root {
    --pack-yellow: #ffd200;
    --disc-cream: #fff0a3;
    --title-yellow: #ffd51c;
    --ink: #1d1a14;
    --gap-white: #ffffff;
  }
  * { margin: 0; padding: 0; box-sizing: border-box; }
  html, body {
    width: 1200px;
    height: 2405px;
    overflow: hidden;
    background: var(--gap-white);
  }
  .canvas {
    position: relative;
    width: 1200px;
    height: 2405px;
    background: var(--gap-white);
  }
  .panel {
    position: absolute;
    left: 0;
    width: 1200px;
    height: 1197px;
    overflow: hidden;
    background: var(--pack-yellow);
  }
  .panel--front { top: 0; }
  .panel--back { top: 1208px; }
  .disc {
    position: absolute;
    width: 1162px;
    height: 1162px;
    border-radius: 50%;
    background: var(--disc-cream);
  }
  .panel--front .disc { left: 22px; top: -257px; }
  .panel--back .disc { left: 20px; top: 360px; }

  .brand-name {
    position: absolute;
    left: 0;
    top: 170px;
    width: 1200px;
    text-align: center;
    font-family: "Londrina Solid", sans-serif;
    font-weight: 900;
    font-size: 290px;
    line-height: 1;
    letter-spacing: 12px;
    color: var(--title-yellow);
  }
  .product-name {
    position: absolute;
    left: 0;
    top: 548px;
    width: 1200px;
    text-align: center;
    font-family: "Short Stack", cursive;
    font-size: 58px;
    letter-spacing: 30px;
    color: var(--ink);
  }

  .ingredients {
    position: absolute;
    left: 0;
    top: 505px;
    width: 1200px;
    text-align: center;
    color: var(--ink);
    font-family: "Short Stack", cursive;
  }
  .ingredients__heading {
    font-size: 30px;
    letter-spacing: 9px;
    font-weight: 400;
    line-height: 1;
  }
  .ingredients__smile {
    display: block;
    margin: 6px auto 0;
  }
  .ingredients__list {
    list-style: none;
    margin-top: 90px;
    font-size: 38px;
    letter-spacing: 3px;
    line-height: 59px;
    text-transform: uppercase;
  }
</style>
</head>
<body>
  <main class="canvas">
    <section class="panel panel--front" aria-label="Front of pack">
      <div class="disc"></div>
      <h1 class="brand-name">DOVRA'S</h1>
      <p class="product-name">SPICE BLEND</p>
    </section>

    <section class="panel panel--back" aria-label="Back of pack">
      <div class="disc"></div>
      <div class="ingredients">
        <h2 class="ingredients__heading">ingredients:</h2>
        <svg class="ingredients__smile" width="290" height="46" viewBox="0 0 290 46" aria-hidden="true">
          <path d="M6 8 Q145 70 284 8" fill="none" stroke="var(--ink)" stroke-width="3" stroke-linecap="round"/>
        </svg>
        <ul class="ingredients__list">
          <li>Cumin</li>
          <li>Coriander</li>
          <li>Dried Red Chili</li>
          <li>Cinnamon</li>
          <li>Cloves</li>
          <li>Cardamon</li>
          <li>Black Peppercorns</li>
          <li>Rice</li>
        </ul>
      </div>
    </section>
  </main>
</body>
</html>
```